Business Card Design Project

I am looking for a minimal matte background/shiny (spot UV) ink monochromatic design with a splash of neon color.

the card should be 2 sided, logo only on one side - all info and possibly logo on the other.

My creative director described the colors he imagined for the design to be:
'it's a dark field, like charcoal or a really dark burgundy, or deep blue, shot through with a neon—but just a tiny bit of it. so a charcoal field with a laser-thin streak of electric lime, safety orange, or cobalt blue. really beautiful stuff.'

here are some samples of the types of cards I am trying to create:
http://www.pictavault.example/photos/dawnpress/6967376935/in/photostream -> Vandrelle Lustre

http://www.pictavault.example/photos/dawnpress/6497659409/in/photostream -> Standard Coated (14pt/matte) with SPOT UV

http://www.pictavault.example/photos/dawnpress/6497658995/in/photostream/ -> Heavy Corvane with Raised Ink

http://www.pictavault.example/photos/dawnpress/6275629165/in/photostream/ -> Standard Coated (14pt/matte) with SPOT UV

Here is my logo:
https://www.filecrate.example/s/sigym192mlh58ge/quillorb%20logotype%20final.ai

Here are the details for info:
Dorian Elwood Marsh
email - dorian@quillorb.example
mobile - 555 013 2867
web -
quillorb.example: inventive technology applications
quillorb-tv.example: innovative video advertising

please let me know if there is anything at all that you need.

Target Market(s)

mid to large agencies that require interactive design and entrepreneurial/startup individuals/companies that need application development.

Industry/Entity Type

Safety

Requirements
Must have
• logo only on one side

```html
<!DOCTYPE html>
<html lang="en">
<head>
<meta charset="utf-8">
<title>Quillorb Business Card</title>
<link rel="stylesheet" href="https://fonts.googleapis.com/css2?family=Poppins:wght@600&family=Quicksand:wght@400;500&display=swap">
<style>
  :root {
    --stage: #1b1b1d;
    --blue-light: #234a9c;
    --blue-mid: #17387f;
    --blue-deep: #0e2762;
    --silver: #dfe2ea;
    --white: #ffffff;
    --ink: #2a2a2e;
    --ink-soft: #3a3a40;
    --rule: #b9bcc4;
    --arrow: #8a8d95;
  }
  * { box-sizing: border-box; margin: 0; padding: 0; }
  html, body { width: 1200px; height: 1200px; overflow: hidden; }
  body { background: var(--stage); position: relative; }

  .card {
    position: absolute;
    left: 160px;
    width: 880px;
    height: 500px;
    overflow: hidden;
    box-shadow: 0 14px 30px rgba(0,0,0,.45);
  }
  .card--front {
    top: 60px;
    background: radial-gradient(ellipse at 55% 40%, var(--blue-light) 0%, var(--blue-mid) 55%, var(--blue-deep) 100%);
  }
  .card--back { top: 640px; background: var(--white); }

  .brand {
    position: absolute;
    display: flex;
    align-items: center;
    transform: translateX(-50%);
    white-space: nowrap;
  }
  .brand__name {
    font-family: 'Poppins', sans-serif;
    font-weight: 600;
    color: var(--silver);
    line-height: 1;
  }
  .brand__dot { background: var(--silver); border-radius: 50%; }

  .card--front .brand { left: 50%; top: 200px; }
  .card--front .brand__name { font-size: 68px; }
  .card--front .brand__dot { width: 18px; height: 18px; margin-left: 16px; }

  .back__field { position: absolute; inset: 0; width: 880px; height: 500px; }

  .card--back .brand { left: 53%; top: 86px; }
  .card--back .brand__name { font-size: 24px; }
  .card--back .brand__dot { width: 8px; height: 8px; margin-left: 7px; }

  .holder {
    position: absolute;
    left: 53%;
    top: 130px;
    transform: translateX(-50%);
    font-family: 'Poppins', sans-serif;
    font-weight: 600;
    font-size: 38px;
    color: var(--white);
    white-space: nowrap;
  }
  .holder__rule {
    position: absolute;
    left: 305px;
    top: 196px;
    width: 320px;
    height: 2px;
    background: linear-gradient(90deg, transparent, rgba(255,255,255,.35), transparent);
  }

  .contact {
    position: absolute;
    left: 50px;
    top: 393px;
    font-family: 'Quicksand', sans-serif;
    font-size: 25px;
    color: var(--ink-soft);
  }
  .contact__row { display: flex; align-items: center; height: 40px; }
  .contact__icon { width: 30px; margin-right: 14px; }
  .contact__row strong { font-weight: 500; color: var(--ink); margin-right: 7px; }

  .divider {
    position: absolute;
    left: 418px;
    top: 298px;
    width: 3px;
    height: 175px;
    background: linear-gradient(180deg, var(--rule), #8f929a, var(--rule));
  }

  .web {
    position: absolute;
    left: 440px;
    top: 300px;
    width: 430px;
    height: 190px;
  }
  .web__domain {
    position: absolute;
    left: 4px;
    font-family: 'Poppins', sans-serif;
    font-weight: 600;
    font-size: 23px;
    line-height: 30px;
    color: var(--ink);
    white-space: nowrap;
  }
  .web__desc {
    position: absolute;
    left: 0;
    font-family: 'Quicksand', sans-serif;
    font-weight: 400;
    font-size: 23px;
    line-height: 30px;
    color: var(--ink-soft);
    white-space: nowrap;
  }
  .web__arrows { position: absolute; inset: 0; }
</style>
</head>
<body>

<section class="card card--front" aria-label="Card front">
  <div class="brand">
    <span class="brand__name">Quillorb</span>
    <span class="brand__dot"></span>
  </div>
</section>

<section class="card card--back" aria-label="Card back">
  <svg class="back__field" viewBox="0 0 880 500" aria-hidden="true">
    <defs>
      <linearGradient id="fieldBlue" x1="0" y1="0" x2="1" y2="0.4">
        <stop offset="0" stop-color="#0f2a6c"/>
        <stop offset=".55" stop-color="#1b3f8c"/>
        <stop offset="1" stop-color="#0f2a6a"/>
      </linearGradient>
    </defs>
    <path d="M0 0 H880 V245 H300 C180 245 70 262 0 300 Z" fill="url(#fieldBlue)"/>
  </svg>

  <div class="brand">
    <span class="brand__name">Quillorb</span>
    <span class="brand__dot"></span>
  </div>
  <h1 class="holder">Dorian Elwood Marsh</h1>
  <div class="holder__rule"></div>

  <div class="contact">
    <div class="contact__row">
      <svg class="contact__icon" viewBox="0 0 30 20" aria-hidden="true">
        <rect x="1" y="2" width="28" height="16" fill="#3a3a40"/>
        <path d="M1 2 L15 12 L29 2" fill="none" stroke="#fff" stroke-width="1.6"/>
      </svg>
      <span>dorian@quillorb.example</span>
    </div>
    <div class="contact__row">
      <svg class="contact__icon" viewBox="0 0 30 30" aria-hidden="true">
        <rect x="7" y="2" width="16" height="26" rx="2.5" fill="none" stroke="#3a3a40" stroke-width="2.4"/>
        <line x1="10" y1="23" x2="20" y2="23" stroke="#3a3a40" stroke-width="1.6"/>
      </svg>
      <span><strong>+555</strong>013 2867</span>
    </div>
  </div>

  <div class="divider"></div>

  <div class="web">
    <span class="web__domain" style="top:0">quillorb.example</span>
    <span class="web__desc" style="top:56px">inventive technology applications</span>
    <span class="web__domain" style="top:88px">quillorb-tv.example</span>
    <span class="web__desc" style="top:150px">innovative video advertising</span>
    <svg class="web__arrows" viewBox="0 0 430 190" aria-hidden="true">
      <path d="M218 18 C232 20 238 32 234 48" fill="none" stroke="var(--arrow)" stroke-width="1.4"/>
      <path d="M229 43 L234 50 L239 43" fill="none" stroke="var(--arrow)" stroke-width="1.4"/>
      <path d="M22 146 C10 142 8 130 13 120" fill="none" stroke="var(--arrow)" stroke-width="1.4"/>
      <path d="M8 125 L13 118 L18 124" fill="none" stroke="var(--arrow)" stroke-width="1.4"/>
    </svg>
  </div>
</section>

</body>
</html>
```